Poster for pawn shop lobby

Looking for green and gold as my colors, like the picture shown of my old poster. This time I'm contemplating with doing pictures as well as just text. Here are ideas of things I buy and give loans on. We want to emphasize jewelry, laptops, game systems, tools. I'm open-minded.
Old & Broken Gold
Jewelry & Collectibles
Diamonds
Video Games & Systems
Up-to-date Computers & Laptops
Tablets
Cameras
Power Tools
Home & Garden Equipment
Sports Equipment
Watches
Antique Collectibles
Musical Instruments
And anything else of value
Shop

```html
<!DOCTYPE html>
<html lang="en">
<head>
<meta charset="utf-8">
<title>We'll Loan or Pay You Cash On</title>
<link href="https://fonts.googleapis.com/css2?family=Archivo+Black&family=Arimo:wght@700&family=Lora:ital,wght@1,700&display=swap" rel="stylesheet">
<style>
  :root {
    --field-green: #3db54a;
    --panel-green: #8cc63f;
    --grass-dark: #1f7a2c;
    --gold: #b49a5c;
    --gold-light: #d6c08a;
    --gold-deep: #8f7640;
    --ink: #1c1c1a;
    --outline-green: #2e9c3e;
    --coin-gold: #e0a526;
    --silver: #dfe6ee;
    --bag-white: #f1f1ee;
    --cash-green: #a9b79a;
  }
  * { margin: 0; padding: 0; box-sizing: border-box; }
  html, body { width: 848px; height: 1200px; overflow: hidden; }
  body { background: var(--field-green); }
  .poster {
    position: relative;
    width: 848px;
    height: 1200px;
    overflow: hidden;
    background: var(--field-green);
    font-family: "Arimo", Arial, sans-serif;
    color: var(--ink);
  }
  .header-band {
    position: absolute; left: 0; top: 0; width: 848px; height: 185px;
    background: linear-gradient(180deg, var(--gold-light) 0%, var(--gold) 55%, var(--gold-deep) 100%);
  }
  .headline {
    position: absolute; left: 0; width: 848px; text-align: center;
    font-family: "Archivo Black", "Arial Black", sans-serif;
    font-size: 68px; line-height: 1; letter-spacing: 1px;
    color: var(--ink);
    text-shadow:
      3px 0 0 var(--outline-green), -3px 0 0 var(--outline-green),
      0 3px 0 var(--outline-green), 0 -3px 0 var(--outline-green),
      2px 2px 0 var(--outline-green), -2px -2px 0 var(--outline-green),
      2px -2px 0 var(--outline-green), -2px 2px 0 var(--outline-green);
  }
  .headline-first { top: 32px; }
  .headline-second { top: 99px; }
  .grass {
    position: absolute; left: 0; top: 1020px; width: 848px; height: 180px;
    background: linear-gradient(180deg, rgba(31,122,44,0) 0%, var(--grass-dark) 60%, #145a1f 100%);
  }
  .item-panel { position: absolute; left: 0; top: 0; width: 848px; height: 1200px; }
  .art { position: absolute; }
  .dollar-sign { width: 64px; height: 120px; border-radius: 14px; background: linear-gradient(180deg, #f6cf55, var(--coin-gold) 60%, #b27a12); }
  .dollar-left { left: 64px; top: 214px; }
  .dollar-right { left: 722px; top: 214px; }
  .diamond { width: 98px; height: 56px; border-radius: 8px; background: linear-gradient(180deg, #ffffff, var(--silver) 60%, #b8c2cc); }
  .diamond-left { left: 207px; top: 397px; }
  .diamond-right { left: 542px; top: 397px; }
  .money-bag { left: 57px; top: 620px; width: 178px; height: 206px; border-radius: 60px 60px 40px 40px; background: linear-gradient(180deg, #ffffff, var(--bag-white) 60%, #c9c9c4); }
  .cash-stack { left: 605px; top: 634px; width: 200px; height: 192px; border-radius: 10px; background: linear-gradient(160deg, #d6dccb, var(--cash-green) 60%, #7f8f70); }
  .line {
    position: absolute; left: 0; width: 848px; text-align: center;
    line-height: 1; white-space: nowrap; color: var(--ink);
  }
  .size-s { font-size: 37px; }
  .size-m { font-size: 41px; }
  .size-l { font-size: 57px; }
  .closing {
    font-family: "Lora", Georgia, serif; font-style: italic; font-weight: 700;
    font-size: 39px;
  }
</style>
</head>
<body>
<div class="poster">
  <div class="header-band"></div>
  <div class="headline headline-first">WE’LL LOAN OR</div>
  <div class="headline headline-second">PAY YOU CASH ON</div>

  <div class="grass" role="img" aria-label="Tall green grass along the bottom edge"></div>

  <svg class="item-panel" width="848" height="1200" viewBox="0 0 848 1200" aria-hidden="true">
    <polygon points="207,218 641,218 829,634 556,634 556,838 758,838 758,1172 88,1172 88,838 292,838 292,634 17,634"
             fill="var(--panel-green)" stroke="var(--gold)" stroke-width="9" stroke-linejoin="miter"/>
    <polygon points="214,227 634,227 815,626 548,626 548,846 750,846 750,1164 96,1164 96,846 300,846 300,626 31,626"
             fill="none" stroke="var(--gold-deep)" stroke-width="1.5"/>
    <rect x="107" y="1092" width="634" height="74" fill="var(--gold-light)" stroke="var(--gold-deep)" stroke-width="2"/>
  </svg>

  <div class="art dollar-sign dollar-left" role="img" aria-label="Shiny gold dollar sign"></div>
  <div class="art dollar-sign dollar-right" role="img" aria-label="Shiny gold dollar sign"></div>
  <div class="art diamond diamond-left" role="img" aria-label="Sparkling cut diamond"></div>
  <div class="art diamond diamond-right" role="img" aria-label="Sparkling cut diamond"></div>
  <div class="art money-bag" role="img" aria-label="White money bag marked with a gold dollar sign"></div>
  <div class="art cash-stack" role="img" aria-label="Fanned stack of hundred dollar bills"></div>

  <div class="line size-s" style="top:256px;">Old &amp; Broken Gold</div>
  <div class="line" style="top:318px;"><span class="size-l">Jewelry</span> <span class="size-s">&amp; Collectibles</span></div>
  <div class="line size-s" style="top:396px;">Diamonds</div>
  <div class="line" style="top:454px;"><span class="size-s">Video</span> <span class="size-l">Games &amp; Systems</span></div>
  <div class="line" style="top:539px;"><span class="size-s">Up-to-date Computers &amp;</span> <span class="size-l">Laptops</span></div>
  <div class="line size-m" style="top:611px;">Tablets</div>
  <div class="line size-m" style="top:670px;">Watches</div>
  <div class="line size-m" style="top:729px;">Cameras</div>
  <div class="line size-m" style="top:789px;">Power Tools</div>
  <div class="line size-m" style="top:846px;">Home &amp; Garden Equipment</div>
  <div class="line size-s" style="top:906px;">Sports Equipment</div>
  <div class="line size-s" style="top:963px;">Antique Collectibles</div>
  <div class="line size-s" style="top:1022px;">Musical Instruments</div>
  <div class="line closing" style="top:1108px;">And anything else of value</div>
</div>
</body>
</html>
```